Business Card for Dental Office - "online review card"

I would like to develop a tasteful card (that would compliment my existing business card) that provides my patients a written link to a portal on my website that would facilitate the generation of online reviews.

My existing business card was a Pixelharbor project a few years ago and has been well received. I hope that it is easily accessed online for reference.

Target Market(s)

Existing patients who need guidance in accessing the "write a review" section of my website

Industry/Entity Type

Business

Requirements
Must have
• -a similar look to my existing card:
http://www.pixelharbor-example.com.au/contest.aspx?id=5192&page=7

-a link to the following url in writing:
http://www.lindqvardental-example.com/reviews.html

- a reference to "appreciating feedback" or "how are we doing?"

```html
<!DOCTYPE html>
<html lang="en">
<head>
<meta charset="utf-8">
<title>Elias R Lindqvar, DDS – Review Card</title>
<link rel="stylesheet" href="https://fonts.googleapis.com/css2?family=Arimo:wght@400&display=swap">
<style>
  :root {
    --backdrop: #4a3536;
    --card-white: #ffffff;
    --ink-purple: #3d3477;
    --brand-cyan: #1aa0dc;
    --back-cyan: #009fdf;
    --band-deep: #3a2f6e;
    --band-mid: #45398a;
    --band-blue: #1e7bbf;
    --mark-fill: #4b3f96;
    --mark-edge: #2d2a5a;
    --text-light: #ffffff;
  }
  * { box-sizing: border-box; margin: 0; padding: 0; }
  html, body { width: 1200px; height: 900px; overflow: hidden; }
  body {
    background: var(--backdrop);
    font-family: "Arimo", Arial, sans-serif;
    position: relative;
  }
  .card {
    position: absolute;
    left: 255px;
    width: 690px;
    height: 395px;
    border-radius: 30px;
    overflow: hidden;
  }
  .card--front { top: 37px; background: var(--card-white); }
  .card--back { top: 465px; background: var(--back-cyan); }

  .front__band { position: absolute; left: 0; top: 0; width: 690px; height: 395px; }

  .brand-square {
    position: absolute;
    left: 45px; top: 52px;
    width: 116px; height: 114px;
    border-radius: 18px;
    background: var(--mark-fill);
    border: 5px solid var(--card-white);
    box-shadow: 0 0 0 2px var(--mark-edge);
  }
  .front__name {
    position: absolute;
    left: 182px; top: 52px;
    font-size: 35px;
    color: var(--ink-purple);
    white-space: nowrap;
  }
  .front__name .credential { font-size: 24px; }
  .front__tagline {
    position: absolute;
    left: 184px; top: 92px;
    font-size: 16.5px;
    letter-spacing: 2.2px;
    color: var(--brand-cyan);
    white-space: nowrap;
  }

  .contact-list { position: absolute; left: 36px; top: 193px; list-style: none; }
  .contact-list li {
    display: flex; align-items: center;
    height: 37px;
    color: var(--text-light);
    font-size: 18px;
  }
  .contact-list svg { width: 30px; height: 30px; margin-right: 13px; flex: none; }

  .address {
    position: absolute;
    left: 380px; top: 283px;
    display: flex; align-items: center;
    color: var(--text-light);
    font-size: 18px;
    line-height: 23px;
  }
  .address svg { width: 24px; height: 38px; margin-right: 10px; }

  .review-line {
    position: absolute;
    left: 0; right: 0; top: 360px;
    text-align: center;
    font-size: 17px;
    color: var(--brand-cyan);
  }
  .review-line .gap { display: inline-block; width: 10px; }

  .brand-square--large {
    left: 243px; top: 78px;
    width: 203px; height: 200px;
    border-radius: 32px;
    border-width: 5px;
  }
  .back__name {
    position: absolute;
    left: 0; right: 0; top: 287px;
    text-align: center;
    font-size: 20px;
    color: var(--ink-purple);
  }
  .back__name .credential { font-size: 13px; }
  .back__tagline {
    position: absolute;
    left: 0; right: 0; top: 309px;
    text-align: center;
    font-size: 8.5px;
    letter-spacing: 2px;
    color: var(--text-light);
  }
</style>
</head>
<body>

<section class="card card--front">
  <svg class="front__band" viewBox="0 0 690 395" aria-hidden="true">
    <defs>
      <linearGradient id="bandGradient" x1="0" y1="0" x2="1" y2="0">
        <stop offset="0" stop-color="var(--band-deep)"/>
        <stop offset="0.55" stop-color="var(--band-mid)"/>
        <stop offset="0.85" stop-color="#3b5aa8"/>
        <stop offset="1" stop-color="var(--band-blue)"/>
      </linearGradient>
    </defs>
    <path d="M0 58 C60 90 110 140 170 148 C300 160 450 110 580 130 C630 138 665 148 690 158 L690 350 L0 350 Z" fill="url(#bandGradient)"/>
  </svg>

  <div class="brand-square"></div>
  <h1 class="front__name">Elias R Lindqvar, <span class="credential">DDS</span></h1>
  <p class="front__tagline">FAMILY AND COSMETIC DENTISTRY</p>

  <ul class="contact-list">
    <li>
      <svg viewBox="0 0 30 30" aria-hidden="true"><path d="M3 11 C3 5 27 5 27 11 L27 13 L21 13 L21 10 L9 10 L9 13 L3 13 Z M8 14 L22 14 L26 25 L4 25 Z" fill="#fff"/><circle cx="15" cy="19.5" r="3" fill="var(--band-deep)"/></svg>
      410 555 0142
    </li>
    <li>
      <svg viewBox="0 0 30 30" aria-hidden="true"><rect x="8" y="1" width="14" height="28" rx="3" fill="none" stroke="#fff" stroke-width="2"/><rect x="10" y="5" width="10" height="17" fill="#fff"/><circle cx="15" cy="25.5" r="1.5" fill="#fff"/></svg>
      410 555 0187
    </li>
    <li>
      <svg viewBox="0 0 30 30" aria-hidden="true"><rect x="2" y="6" width="26" height="18" fill="none" stroke="#fff" stroke-width="2"/><path d="M2 6 L15 17 L28 6 M2 24 L12 14 M28 24 L18 14" fill="none" stroke="#fff" stroke-width="2"/></svg>
      eliaslindqvar@examplemail.com
    </li>
    <li>
      <svg viewBox="0 0 30 30" aria-hidden="true"><g fill="none" stroke="#fff" stroke-width="1.8"><circle cx="15" cy="15" r="13"/><ellipse cx="15" cy="15" rx="6" ry="13"/><path d="M15 2 V28 M2 15 H28 M4 8 H26 M4 22 H26"/></g></svg>
      lindqvardental-example.com
    </li>
  </ul>

  <div class="address">
    <svg viewBox="0 0 24 38" aria-hidden="true"><path d="M12 1 C5 1 1 6 1 12 C1 20 12 37 12 37 C12 37 23 20 23 12 C23 6 19 1 12 1 Z" fill="#fff"/></svg>
    <p>14 Harbor Mill Court, 210<br>Brookfield, Maryland 21000</p>
  </div>

  <p class="review-line">how are we doing?<span class="gap"></span>www.lindqvardental-example.com/reviews.html</p>
</section>

<section class="card card--back">
  <div class="brand-square brand-square--large"></div>
  <h2 class="back__name">Elias R. Lindqvar, <span class="credential">DDS</span></h2>
  <p class="back__tagline">FAMILY AND COSMETIC DENTISTRY</p>
</section>

</body>
</html>
```